Singer Song writer needs a CD cover Design

I need a cover design to a 4 pages digipak. ( Front, inside, CD-tray and back) And a digital cover art. And a design for the CD

I want it clear and simple. The name of my album is "Bølgeslag" which means refleksions in danish. I play folk-rock, pop and country

I don't no about the pictures. Maybe you can use it somewhere in the design. And maybe not.
Updates

I like the designs I have received so far. Thank you very much for a god job.I was wondering if some of you would try to make a design without my pictures. Where you can create your own interpretation of the title "Bølgeslagene". It could be very interesting to see your meaning of that word.Bølgeslagene means reflections in danish.You can make reflections over your life. Think about how you are living. But you can also reflect a light. The way we are living and what we are doing in life - are making light reflections.Does it make sense?Best regardsBrian Added Friday, November 20, 2015

Industry/Entity Type

Digital

Requirements
Must have
• My name and the Album's name:
• Bølgeslag
• Torsten Maltbæk
• A list of the songs
• 1: Mørke og tavse
• 2: Min vej, min sten
• 3: Gå nu ud
• 4: Et par af de glemte
• 5: Før end vi går
• 6: Hvor stille er min have
• 7: Milde Morten
• 8: Sent om året
• 9: En vise om havets bund
• And a description of the album
• Kære lytter
• Bølgeslag består af to dele. Fem sange, der er skrevet over temaet ”refleksioner”. Og en re-mastered udgave af sangene fra lovsangs EP’en ”Under fyrets blink”.
• Jeg håber, du vil sætte dig godt til rette. Nyde et glas eller en kop. Og naturligvis nyde musikken.
• God fornøjelse.
• Medvirkende:
• Torsten Maltbæk: Vokal, klaver, akustisk guitar på #1 #2 #4 #5, kor på #1 #2 #3 #4 #5,
• Aksel Brøndum: Bas på #6 #7 #8 #9, elguitar på #1 #2 #3 #4
• Niels Tofting Krag: Bas på #1 #2 #3 #4
• Tobias Hvilsom Larsen: Trommer
• Mogens Sønderby Holm: Akustisk guitar på #7 #8 #9, elguitar på #6 #8 #9, Lab Steel på #7 #9, Mandolin på #9
• Karsten Møllvig Tang: Elguitar på #1 #2 #4, akustisk guitar på #3
• Lis-Marie Hedda Skovlund: kor på #6 #7 #8 #9, vokal på #6 og #9
• Indspillet i Grønbro Studio af Ulrik Stenbæk Dahlgaard og Karsten Møllvig Tang
• Mikset og produceret af Karsten Møllvig Tang
• Alle sange er skrevet og komponeret af Torsten Maltbæk
Nice to have
• Interpretations of the word reflections

```html
<!DOCTYPE html>
<html lang="da">
<head>
<meta charset="utf-8">
<title>Bølgeslag – Digipak layout</title>
<link href="https://fonts.googleapis.com/css2?family=Archivo+Black&family=Open+Sans:ital,wght@0,400;0,600;0,700;0,800;1,400;1,600;1,700&family=Roboto:wght@400&display=swap" rel="stylesheet">
<style>
  :root {
    --paper: #ffffff;
    --ink: #111111;
    --white: #ffffff;
    --spine: #0a0a0a;
    --disc-rim: #d9d9d9;
  }
  * { box-sizing: border-box; margin: 0; padding: 0; }
  html, body { width: 1200px; height: 1200px; overflow: hidden; background: var(--paper); }
  body { position: relative; font-family: "Open Sans", sans-serif; color: var(--ink); }

  .panel-label {
    position: absolute;
    font-family: "Archivo Black", sans-serif;
    font-size: 38px;
    line-height: 1;
    letter-spacing: 0.5px;
    text-align: center;
    width: 540px;
  }
  .label-inner-right { left: 53px; top: 60px; }
  .label-inner-left { left: 613px; top: 60px; }
  .label-back { left: 53px; top: 1088px; }
  .label-front { left: 605px; top: 1088px; }

  .panel { position: absolute; overflow: hidden; }

  /* Inner right – disc tray */
  .tray { left: 53px; top: 105px; width: 536px; height: 482px; }
  .tray svg { display: block; }
  .disc-title {
    position: absolute; left: 94px; top: 166px;
    font-weight: 700; font-size: 27px; color: var(--white);
  }
  .disc-tracks {
    position: absolute; left: 325px; top: 243px;
    list-style: none; font-size: 9.2px; font-weight: 600; line-height: 13px; color: var(--white);
  }

  /* Inner left – credits */
  .credits { left: 607px; top: 105px; width: 536px; height: 482px; color: var(--white); }
  .credits-bg { position: absolute; inset: 0; }
  .credits-heading {
    position: absolute; right: 20px; top: 22px;
    font-size: 15px; font-weight: 700; font-style: italic;
  }
  .credit-list { position: absolute; left: 24px; top: 100px; width: 200px; list-style: none; }
  .credit-list li { font-size: 12.4px; line-height: 17.5px; margin-bottom: 17px; }
  .credit-list strong { font-weight: 700; }

  /* Back */
  .back { left: 53px; top: 589px; width: 536px; height: 480px; color: var(--white); }
  .back-bg { position: absolute; inset: 0; }
  .back-frame { position: absolute; left: 10px; top: 10px; right: 12px; bottom: 10px; border: 1px solid rgba(255,255,255,0.12); }
  .back-title { position: absolute; left: 30px; top: 12px; font-size: 37px; font-weight: 800; letter-spacing: -0.5px; }
  .back-letter {
    position: absolute; left: 32px; top: 56px; width: 260px;
    font-size: 15.5px; font-style: italic; line-height: 21.8px;
  }
  .back-tracks {
    position: absolute; left: 320px; top: 56px; list-style: none;
    font-size: 15.5px; font-weight: 700; font-style: italic; line-height: 21.8px;
  }
  .back-tracks span { display: inline-block; width: 17px; font-weight: 600; }
  .credit-line { position: absolute; font-size: 12px; line-height: 17.5px; }
  .credit-line em { font-weight: 700; }
  .credit-studio { left: 32px; top: 329px; }
  .credit-mix { right: 25px; top: 366px; text-align: right; }
  .credit-writer { left: 0; width: 536px; top: 410px; text-align: center; }

  /* Spine */
  .spine { left: 589px; top: 589px; width: 22px; height: 480px; background: var(--spine); }
  .spine-title {
    position: absolute; left: 50%; top: 180px;
    transform: translateX(-50%) rotate(90deg); transform-origin: center;
    white-space: nowrap; font-size: 15px; font-weight: 800; color: var(--white);
    width: 120px; text-align: center; margin-left: 0;
  }

  /* Front */
  .front { left: 611px; top: 589px; width: 536px; height: 480px; }
  .front-bg { position: absolute; inset: 0; }
  .front-title {
    position: absolute; left: 52px; top: 95px;
    font-size: 74px; font-weight: 800; color: var(--ink); letter-spacing: -1px;
    transform: rotate(-18deg) skewX(-4deg); transform-origin: left bottom; white-space: nowrap;
  }

  .draft-note {
    position: absolute; left: 28px; top: 1151px;
    font-family: "Roboto", sans-serif; font-size: 14px; line-height: 18px; letter-spacing: 0.4px;
  }
</style>
</head>
<body>

<div class="panel-label label-inner-right">INNER RIGHT</div>
<div class="panel-label label-inner-left">INNER LEFT</div>

<section class="panel tray">
  <svg width="536" height="482" viewBox="0 0 536 482">
    <defs>
      <linearGradient id="tray-photo" x1="0" y1="0" x2="1" y2="1">
        <stop offset="0" stop-color="#6d6a66"/>
        <stop offset="0.5" stop-color="#a9a6a1"/>
        <stop offset="1" stop-color="#3e3c3a"/>
      </linearGradient>
      <radialGradient id="disc-photo" cx="0.5" cy="0.45" r="0.6">
        <stop offset="0" stop-color="#6a6764"/>
        <stop offset="0.55" stop-color="#a8a5a0"/>
        <stop offset="1" stop-color="#d5d3cf"/>
      </radialGradient>
    </defs>
    <rect width="536" height="482" fill="url(#tray-photo)" role="img" aria-label="Black and white photo of a musician seated at a piano"/>
    <circle cx="270" cy="242" r="233" fill="var(--disc-rim)"/>
    <circle cx="270" cy="242" r="226" fill="url(#disc-photo)" role="img" aria-label="Disc print: black and white photo of a wooden bench"/>
    <circle cx="270" cy="242" r="40" fill="#ececec"/>
    <circle cx="270" cy="242" r="35" fill="#3a3836" role="img" aria-label="Piano detail photo in the disc centre"/>
  </svg>
  <div class="disc-title">Bølgeslag</div>
  <ol class="disc-tracks">
    <li>1 Mørke og tavse</li>
    <li>2 Min vej, min sten</li>
    <li>3 Gå nu ud</li>
    <li>4 Et par af de glemte</li>
    <li>5 Før end vi går</li>
    <li>6 Hvor stille er min have</li>
    <li>7 Milde Morten</li>
    <li>8 Sent om året</li>
    <li>9 En vise om havets bund</li>
  </ol>
</section>

<section class="panel credits">
  <svg class="credits-bg" width="536" height="482" viewBox="0 0 536 482" role="img" aria-label="Concert photo of the band performing on a blue-lit stage">
    <defs>
      <linearGradient id="stage-photo" x1="0" y1="0" x2="1" y2="1">
        <stop offset="0" stop-color="#1a1712"/>
        <stop offset="0.35" stop-color="#2b2a48"/>
        <stop offset="0.7" stop-color="#5a3a1c"/>
        <stop offset="1" stop-color="#2a1a0c"/>
      </linearGradient>
    </defs>
    <rect width="536" height="482" fill="url(#stage-photo)"/>
  </svg>
  <div class="credits-heading">Medvirkende:</div>
  <ul class="credit-list">
    <li><strong>Torsten Maltbæk:</strong> Vokal, klaver, akustisk guitar på #1 #2 #4 #5, kor på #1 #2 #3 #4 #5</li>
    <li><strong>Aksel Brøndum:</strong> Bas på #6 #7 #8 #9, elguitar på #1 #2 #3 #4</li>
    <li><strong>Niels Krag:</strong> Bas på #1 #2 #3 #4</li>
    <li><strong>Tobias Larsen:</strong> Trommer</li>
    <li><strong>Mogens Sønderby Holm:</strong> Akustisk guitar på #7 #8 #9, elguitar på #6 #8 #9, Lab Steel på #7 #9, Mandolin på #9</li>
    <li><strong>Karsten Møllvig Tang:</strong> Elguitar på #1 #2 #4</li>
    <li><strong>Lis-Marie Hedda Skovlund:</strong> kor på #6 #7 #8 #9, vokal på #6 og #9</li>
  </ul>
</section>

<section class="panel back">
  <svg class="back-bg" width="536" height="480" viewBox="0 0 536 480" role="img" aria-label="Dark photo of interlocking puzzle pieces">
    <defs>
      <radialGradient id="puzzle-photo" cx="0.6" cy="0.75" r="0.8">
        <stop offset="0" stop-color="#4a4a55"/>
        <stop offset="0.6" stop-color="#24242b"/>
        <stop offset="1" stop-color="#0e0e12"/>
      </radialGradient>
    </defs>
    <rect width="536" height="480" fill="url(#puzzle-photo)"/>
  </svg>
  <div class="back-frame"></div>
  <h1 class="back-title">Bølgeslag</h1>
  <p class="back-letter">Kære lytter<br>Bølgeslag består af to dele. Fem sange, der er skrevet over temaet ”Bølgeslag”. Og en re-mastered udgave af sangene fra lovsangs EP’en ”Under fyrets blink”.<br>Jeg håber, du vil sætte dig godt til rette. Nyde et glas eller en kop. Og naturligvis nyde musikken.<br>God fornøjelse.</p>
  <ol class="back-tracks">
    <li><span>1</span> Mørke og tavse</li>
    <li><span>2</span> Min vej, min sten</li>
    <li><span>3</span> Gå nu ud</li>
    <li><span>4</span> Et par af de glemte</li>
    <li><span>5</span> Før end vi går</li>
    <li><span>6</span> Hvor stille er min have</li>
    <li><span>7</span> Milde Morten</li>
    <li><span>8</span> Sent om året</li>
  </ol>
  <p class="credit-line credit-studio">Indspillet i Grønbro Studio af<br><em>Ulrik Stenbæk Dahlgaard</em> og <em>Karsten Møllvig</em></p>
  <p class="credit-line credit-mix">Mikset og produceret af<br><em>Karsten Møllvig Tang</em></p>
  <p class="credit-line credit-writer">Alle sange er skrevet og komponeret af<br><em>Torsten Maltbæk</em></p>
</section>

<section class="panel spine">
  <div class="spine-title">Bølgeslag</div>
</section>

<section class="panel front">
  <svg class="front-bg" width="536" height="480" viewBox="0 0 536 480" role="img" aria-label="Photo of a man standing among tall wooden posts in a grassy field under a pale sky">
    <defs>
      <linearGradient id="field-photo" x1="0" y1="0" x2="0" y2="1">
        <stop offset="0" stop-color="#f1efe2"/>
        <stop offset="0.45" stop-color="#e4e2d0"/>
        <stop offset="0.6" stop-color="#9aa56a"/>
        <stop offset="1" stop-color="#6f7f3c"/>
      </linearGradient>
    </defs>
    <rect width="536" height="480" fill="url(#field-photo)"/>
  </svg>
  <div class="front-title">Bølgeslag</div>
</section>

<div class="panel-label label-back">BACK</div>
<div class="panel-label label-front">FRONT</div>

<p class="draft-note">DESIGN IS PRESENTED AS DRAFT<br>AND CAN BE MODIFED UPON REQUEST</p>

</body>
</html>
```